Pine Ridge Golf New Location Postcard

I need a postcard announcing our new location. It is a indoor golf training facility that offers award winner instruction, state-of-the-art technology, and custom club fitting. Whether you are a beginner, an aspiring athlete, or an amateur, Pine Ridge Golf offers personalized programs to help take your game to the next level. Call now to schedule your free tour or to sign up. Limited memberships available.
I would like somewhere are on postcard to say Don't put away your clubs just yet! The course may be closed but Pine Ridge Golf's new indoor location is open!
Training

```html
<!DOCTYPE html>
<html lang="en">
<head>
<meta charset="UTF-8">
<title>Pine Ridge Golf – New Location Postcard</title>
<link href="https://fonts.googleapis.com/css2?family=Righteous&family=Oswald:wght@400;500&family=Roboto+Condensed:wght@300;400&family=Montserrat:wght@400;800;900&family=Quicksand:wght@500&display=swap" rel="stylesheet">
<style>
  :root {
    --red: #e53b35;
    --red-dark: #c92a25;
    --ink: #3a3a3a;
    --grey-dark: #5d5d5d;
    --grey-mid: #9a9a9a;
    --grey-light: #e6e6e6;
    --white: #ffffff;
    --backdrop-a: #d4d4d4;
    --backdrop-b: #9d9d9d;
  }
  * { margin: 0; padding: 0; box-sizing: border-box; }
  html, body { width: 918px; height: 1200px; overflow: hidden; }
  body {
    position: relative;
    background: radial-gradient(ellipse at center, var(--backdrop-a) 0%, var(--backdrop-b) 100%);
    font-family: "Roboto Condensed", sans-serif;
  }
  .side-label {
    position: absolute; left: 0; width: 100%;
    text-align: center;
    font-family: "Quicksand", sans-serif;
    font-size: 32px; letter-spacing: 1px; color: #111;
  }
  .side-label--front { top: 18px; }
  .side-label--back { top: 1142px; }

  .postcard {
    position: absolute; left: 132px; width: 660px; height: 512px;
    overflow: hidden; background: var(--white);
    box-shadow: 0 4px 12px rgba(0,0,0,0.35);
  }
  .postcard--front { top: 68px; }
  .postcard--back { top: 606px; }
  .postcard svg.art { position: absolute; left: 0; top: 0; }
  .abs { position: absolute; }

  /* front */
  .headline {
    left: 20px; top: 24px; width: 300px;
    font-family: "Righteous", sans-serif; color: var(--white);
    font-size: 23px; line-height: 28px; text-transform: uppercase; white-space: nowrap;
  }
  .subhead {
    left: 17px; top: 95px;
    font-family: "Oswald", sans-serif; color: var(--white);
    font-size: 12.5px; line-height: 16px; text-transform: uppercase;
  }
  .band-url {
    left: 18px; top: 150px;
    font-family: "Roboto Condensed", sans-serif; font-size: 11px;
    letter-spacing: 4px; color: var(--ink);
  }
  .intro {
    left: 16px; top: 250px; width: 290px;
    font-weight: 300; font-size: 12px; line-height: 15.2px; color: var(--ink);
  }
  .cta {
    left: 59px; top: 357px;
    font-family: "Montserrat", sans-serif; font-weight: 900;
    font-size: 18px; line-height: 19px; color: var(--red); text-transform: uppercase;
  }
  .memberships {
    left: 16px; top: 430px;
    font-family: "Montserrat", sans-serif; font-weight: 900;
    font-size: 21px; color: var(--ink); text-transform: uppercase;
  }
  .footer-url {
    right: 27px; top: 480px;
    font-family: "Montserrat", sans-serif; font-size: 13px; color: var(--white);
  }
  .brand-badge {
    left: 348px; top: 208px; width: 160px; height: 160px;
    display: flex; align-items: center; justify-content: center; text-align: center;
    font-family: "Righteous", sans-serif; font-size: 25px; line-height: 28px;
    color: var(--red);
  }

  /* back */
  .contact-title {
    left: 20px; top: 24px;
    font-family: "Righteous", sans-serif; color: var(--white);
    font-size: 23px; text-transform: uppercase; line-height: 24px;
  }
  .contact-title strong {
    display: block; font-family: "Montserrat", sans-serif; font-weight: 900;
    font-size: 27px; line-height: 34px;
  }
  .contact-row {
    left: 20px; display: flex; gap: 18px; align-items: center;
    font-family: "Roboto Condensed", sans-serif; font-size: 15px; color: var(--white);
  }
  .contact-row span { display: flex; align-items: center; gap: 6px; }
  .contact-row--one { top: 104px; }
  .contact-row--two { top: 128px; }
  .postage {
    left: 524px; top: 19px; width: 110px; height: 131px;
    border: 1.5px solid var(--grey-mid);
    display: flex; align-items: center; justify-content: center; text-align: center;
    font-family: "Oswald", sans-serif; font-weight: 500; font-size: 15px; line-height: 20px;
    color: var(--ink);
  }
  .map {
    left: 0; top: 179px; width: 320px; height: 243px;
    background: linear-gradient(160deg, #f2f2ef 0%, #e9ebe6 100%);
    border: 2px solid var(--grey-mid); border-left: none;
  }
  .brand-tile {
    left: 0; top: 434px; width: 82px; height: 78px; background: var(--red);
    display: flex; align-items: center; justify-content: center; text-align: center;
    font-family: "Righteous", sans-serif; color: var(--white); font-size: 14px; line-height: 16px;
  }
  .barcode-label {
    left: 300px; top: 458px; width: 160px; text-align: center;
    font-family: "Montserrat", sans-serif; font-weight: 800; font-size: 16px;
    color: var(--grey-mid); letter-spacing: 0.5px;
  }
  .address-line { left: 348px; width: 286px; height: 1px; background: var(--grey-mid); }
</style>
</head>
<body>

<div class="side-label side-label--front">FRONT PAGE</div>

<section class="postcard postcard--front">
  <svg class="art" width="660" height="512" viewBox="0 0 660 512">
    <defs>
      <linearGradient id="paper" x1="0" y1="0" x2="0" y2="1">
        <stop offset="0" stop-color="#ffffff"/><stop offset="1" stop-color="#eeeeee"/>
      </linearGradient>
      <linearGradient id="band" x1="0" y1="0" x2="0" y2="1">
        <stop offset="0" stop-color="#f4f4f4"/><stop offset="1" stop-color="#d0d0d0"/>
      </linearGradient>
      <linearGradient id="sunset" x1="0" y1="0" x2="0" y2="1">
        <stop offset="0" stop-color="#6f8e8a"/><stop offset="0.55" stop-color="#e8c04a"/><stop offset="0.8" stop-color="#4a3a1c"/><stop offset="1" stop-color="#1b1a14"/>
      </linearGradient>
      <radialGradient id="turf" cx="0.5" cy="0.5" r="0.6">
        <stop offset="0" stop-color="#3f8f3b"/><stop offset="1" stop-color="#1f5e22"/>
      </radialGradient>
    </defs>
    <rect width="660" height="512" fill="url(#paper)"/>
    <path d="M10 248 Q 250 275 360 150" fill="none" stroke="#d8d8d8" stroke-width="7" opacity="0.7"/>
    <rect width="660" height="140" fill="var(--red)"/>
    <ellipse cx="150" cy="110" rx="235" ry="118" fill="var(--red)"/>
    <circle cx="500" cy="150" r="140" fill="var(--red)"/>
    <polygon points="0,140 330,140 345,174 0,174" fill="url(#band)"/>
    <line x1="0" y1="88" x2="330" y2="88" stroke="#f06a64" stroke-width="1"/>
    <circle cx="464" cy="100" r="138" fill="var(--white)"/>
    <circle cx="464" cy="100" r="128" fill="url(#sunset)" role="img" aria-label="Photo: golfer silhouette mid-swing against a sunset sky"/>
    <circle cx="566" cy="278" r="142" fill="var(--white)"/>
    <circle cx="566" cy="278" r="132" fill="url(#turf)" role="img" aria-label="Photo: golf driver beside a pink ball on green turf"/>
    <circle cx="428" cy="288" r="80" fill="var(--white)" stroke="var(--red)" stroke-width="9"/>
    <line x1="0" y1="342" x2="380" y2="342" stroke="#dddddd" stroke-width="1"/>
    <line x1="0" y1="414" x2="660" y2="414" stroke="#dddddd" stroke-width="1"/>
    <circle cx="34" cy="378" r="18" fill="var(--grey-dark)"/>
    <path d="M27 370c1-1 3-1 4 0l2 3c0 1 0 2-1 3l-1 1c1 2 3 4 5 5l1-1c1-1 2-1 3-1l3 2c1 1 1 3 0 4l-2 2c-6 1-15-8-14-14z" fill="var(--white)"/>
    <polygon points="0,472 515,472 490,496 270,496 250,512 0,512" fill="var(--grey-dark)"/>
    <polygon points="250,512 270,496 490,496 515,472 660,472 660,512" fill="var(--red-dark)"/>
    <polygon points="520,472 526,472 500,498 494,498" fill="var(--white)" opacity="0.7"/>
  </svg>

  <h1 class="abs headline">Don't put away<br>your clubs just yet!</h1>
  <p class="abs subhead">The course may be closed but Pine Ridge Golf's<br>new indoor location is open!</p>
  <p class="abs band-url">WWW.WEBSITEADDRESS.COM</p>
  <div class="abs brand-badge">Pine Ridge<br>Golf</div>
  <p class="abs intro">It is a indoor golf training facility that offers award winner instruction, state-of-the-art technology, and custom club fitting. Whether you are a beginner, an aspiring athlete, or an amateur, Pine Ridge Golf offers personalized programs to help take your game to the next level.</p>
  <p class="abs cta">Call now to schedule your<br>free tour or to sign up.</p>
  <p class="abs memberships">Limited memberships available.</p>
  <p class="abs footer-url">www.website.com</p>
</section>

<section class="postcard postcard--back">
  <svg class="art" width="660" height="512" viewBox="0 0 660 512">
    <defs>
      <linearGradient id="steel" x1="0" y1="0" x2="0" y2="1">
        <stop offset="0" stop-color="#d6d6d6"/><stop offset="1" stop-color="#9a9a9a"/>
      </linearGradient>
    </defs>
    <rect x="0" y="0" width="496" height="164" fill="var(--red)"/>
    <rect x="496" y="0" width="2" height="164" fill="#cfcfcf"/>
    <line x1="0" y1="86" x2="496" y2="86" stroke="#f06a64" stroke-width="1"/>
    <rect x="0" y="164" width="322" height="15" fill="url(#steel)"/>
    <rect x="0" y="422" width="84" height="12" fill="url(#steel)"/>
  </svg>

  <h2 class="abs contact-title">For more information contact<strong>Pine Ridge Golf Company</strong></h2>
  <div class="abs contact-row contact-row--one">
    <span><svg width="12" height="14" viewBox="0 0 12 14"><path d="M6 0a6 6 0 0 1 6 6c0 4-6 8-6 8S0 10 0 6a6 6 0 0 1 6-6z" fill="#fff"/><circle cx="6" cy="6" r="2.2" fill="var(--red)"/></svg>1480 BIRCHWOOD AVENUE</span>
    <span><svg width="15" height="12" viewBox="0 0 15 12"><path d="M1 4c2-3 11-3 13 0l-1 2-3-1V3H5v2L2 6z" fill="#fff"/><rect x="3" y="7" width="9" height="5" rx="1" fill="#fff"/></svg>123-456-7890</span>
  </div>
  <div class="abs contact-row contact-row--two">
    <span><svg width="15" height="13" viewBox="0 0 15 13"><rect x="3" y="0" width="9" height="4" fill="#fff"/><rect x="0" y="5" width="15" height="8" rx="1" fill="#fff"/><rect x="3" y="8" width="9" height="2" fill="var(--red)"/></svg>123-456-7891</span>
    <span><svg width="14" height="14" viewBox="0 0 14 14"><circle cx="7" cy="7" r="7" fill="#fff"/><rect x="3.5" y="4.5" width="7" height="5" fill="var(--red)"/><path d="M3.5 4.5l3.5 3 3.5-3" stroke="#fff" fill="none"/></svg>info@emailaddress.com</span>
  </div>

  <div class="abs postage">PRSRTSTD<br>ECRWSS<br>U.S.POSTAGE<br>PAID</div>
  <div class="abs map" role="img" aria-label="Street map showing the location of 1480 Birchwood Avenue"></div>

  <div class="abs address-line" style="top:235px"></div>
  <div class="abs address-line" style="top:279px"></div>
  <div class="abs address-line" style="top:318px"></div>
  <div class="abs address-line" style="top:362px"></div>

  <div class="abs brand-tile">Pine Ridge<br>Golf</div>
  <p class="abs barcode-label">BARCODE AREA</p>
</section>

<div class="side-label side-label--back">BACK SIDE</div>

</body>
</html>
```